Business cards for Wendcycle

We need a business card layout for our new bike and e-bike rental (we also sell used e-bikes and bike accessories). The logo already exists.

```html
<!DOCTYPE html>
<html lang="de">
<head>
<meta charset="utf-8">
<title>Wendcycle – Visitenkarten</title>
<link rel="stylesheet" href="https://fonts.googleapis.com/css2?family=Source+Sans+3:wght@300;400;600&display=swap">
<style>
  :root {
    --backdrop: #141414;
    --card: #222222;
    --card-edge: #2c2c2c;
    --ink: #f2f2f2;
    --ink-muted: #b9b9b9;
    --teal: #5ec7a9;
    --blush: #ecd3c7;
    --rule: #4a4a4a;
    --ghost: rgba(255, 255, 255, 0.04);
  }
  * { box-sizing: border-box; margin: 0; padding: 0; }
  html, body { width: 1200px; height: 900px; overflow: hidden; }
  body {
    background: var(--backdrop);
    font-family: "Source Sans 3", "Myriad Pro", Arial, sans-serif;
    color: var(--ink);
    position: relative;
  }
  .card {
    position: absolute;
    left: 280px;
    width: 640px;
    height: 366px;
    background: var(--card);
    border-radius: 22px;
    box-shadow: 0 14px 40px rgba(0, 0, 0, 0.6), inset 0 0 0 1px var(--card-edge);
    overflow: hidden;
  }
  .card--back { top: 70px; }
  .card--front { top: 464px; }

  .ghost-mark {
    position: absolute;
    border-radius: 50%;
    background: var(--ghost);
  }
  .card--back .ghost-mark { width: 240px; height: 240px; left: 110px; top: -30px; }
  .card--front .ghost-mark { width: 170px; height: 170px; left: -40px; top: 20px; }

  .brand { position: absolute; text-align: center; }
  .brand__name {
    font-weight: 300;
    letter-spacing: 0.02em;
    line-height: 1;
  }
  .brand__dot {
    display: block;
    border-radius: 50%;
    width: 14px;
    height: 14px;
    background: var(--blush);
  }
  .brand__tagline {
    font-weight: 600;
    color: var(--blush);
    font-size: 15px;
    margin-top: 8px;
  }

  .card--back .brand { left: 0; right: 0; top: 112px; }
  .card--back .brand__name { font-size: 64px; color: var(--ink); }
  .card--back .brand__dot { margin: 0 auto 12px; }
  .website {
    position: absolute;
    left: 0; right: 0; bottom: 44px;
    text-align: center;
    font-size: 15px;
    letter-spacing: 0.32em;
    color: var(--ink);
  }

  .card--front .brand { right: 44px; top: 34px; text-align: right; }
  .card--front .brand__name { font-size: 62px; color: var(--teal); }
  .card--front .brand__dot { margin: 0 70px 10px auto; }
  .card--front .brand__tagline { text-align: center; margin-right: 30px; }

  .divider {
    position: absolute;
    left: 40px; right: 40px; top: 192px;
    height: 1px;
    background: var(--rule);
  }
  .address {
    position: absolute;
    right: 44px; top: 208px;
    text-align: right;
    font-style: normal;
    font-size: 16px;
    line-height: 1.35;
    color: var(--ink);
  }
  .person { position: absolute; left: 40px; top: 210px; width: 250px; }
  .person__name { font-size: 24px; font-weight: 600; color: var(--teal); line-height: 1.1; }
  .person__role { font-size: 16px; color: var(--ink-muted); margin-top: 2px; }
  .person__rule { height: 1px; background: var(--rule); margin: 10px 0; }
  .contact { list-style: none; font-size: 16px; line-height: 1.35; color: var(--ink-muted); }
  .contact li { display: flex; align-items: center; gap: 7px; }
  .contact svg { width: 13px; height: 13px; fill: var(--teal); flex: none; }
</style>
</head>
<body>

<section class="card card--back" aria-label="Visitenkarte Rückseite">
  <div class="ghost-mark" role="img" aria-label="Dezentes Markenzeichen im Hintergrund"></div>
  <div class="brand">
    <span class="brand__dot"></span>
    <div class="brand__name">WENDCYCLE</div>
    <div class="brand__tagline">e-leicht losrollen</div>
  </div>
  <div class="website">www.wendcycle.de</div>
</section>

<section class="card card--front" aria-label="Visitenkarte Vorderseite">
  <div class="ghost-mark" role="img" aria-label="Dezentes Markenzeichen im Hintergrund"></div>
  <div class="brand">
    <span class="brand__dot"></span>
    <div class="brand__name">WENDCYCLE</div>
    <div class="brand__tagline">e-leicht losrollen</div>
  </div>
  <div class="divider"></div>
  <address class="address">12345, Address Goes Here<br>Country Name, 123456</address>
  <div class="person">
    <div class="person__name">Lena Hartwig</div>
    <div class="person__role">Managing Director</div>
    <div class="person__rule"></div>
    <ul class="contact">
      <li>
        <svg viewBox="0 0 16 16" aria-hidden="true"><path d="M2 5c0-2 2-3 6-3s6 1 6 3v1h-3V5H5v1H2zM4 7h8l2 6H2z"/></svg>
        044-318 207 564
      </li>
      <li>
        <svg viewBox="0 0 16 16" aria-hidden="true"><path d="M4 1h8v14H4zM5.5 3v9h5V3z"/></svg>
        044-318 207 564
      </li>
      <li>
        <svg viewBox="0 0 16 16" aria-hidden="true"><path d="M1 3h14v10H1zM2 4.5v.5l6 4 6-4v-.5z"/></svg>
        hallo@wendcycle.de
      </li>
    </ul>
  </div>
</section>

</body>
</html>
```